Brisket Vantle Orbis Holdings.com

We are doing a full website redesign. Here is a video explanation of what we need https://www.clipvessa.com/share/4b21f09a6ce347d1a85f2e7b90d15c66

THANK YOU SO MUCH!!

Here is a link to our current site
http://www.qentrifold.com

Target Market(s)

Pelwick QRX Sellers

Number of Pages Required

5+ page

Requirements
Must have
• Watch the video and follow the instructions!
• https://www.clipvessa.com/share/4b21f09a6ce347d1a85f2e7b90d15c66

```html
<!DOCTYPE html>
<html lang="en">
<head>
<meta charset="utf-8">
<title>Qentrifold.com — Member Area Screens</title>
<link rel="stylesheet" href="https://fonts.googleapis.com/css2?family=Libre+Baskerville&family=Montserrat:wght@400;500;600;700&display=swap">
<style>
:root{
  --canvas:#e2e3e5;
  --ink:#1c2126;
  --text:#2b2f33;
  --muted:#7b8187;
  --line:#e3e5e8;
  --soft:#f4f5f6;
  --blue:#1c74c9;
  --green:#3aa54a;
  --grey-btn:#5f666d;
  --white:#ffffff;
}
*{box-sizing:border-box;margin:0;padding:0}
html,body{width:1200px;height:2655px;overflow:hidden}
body{background:var(--canvas);font-family:"Montserrat",Arial,sans-serif;color:var(--text);position:relative}
.serif{font-family:"Libre Baskerville",Georgia,serif;font-weight:400}
h1,h2{font-weight:400}
.screen{position:absolute;background:var(--white);overflow:hidden}

/* login */
.login{left:200px;top:198px;width:800px;height:496px;background:#2a2f33}
.login-photo{position:absolute;inset:0;background:linear-gradient(100deg,#c9ccce 0%,#8f9396 28%,#3f4448 55%,#2a2e31 100%)}
.login-card{position:absolute;left:536px;top:98px;width:220px;height:299px;background:var(--white);border-radius:4px;overflow:hidden;box-shadow:0 6px 20px rgba(0,0,0,.3)}
.login-card .card-head{height:55px;background:#3b4044;display:flex;align-items:center;justify-content:center;color:var(--white);font-size:16px}
.login-card .card-body{padding:12px 24px}
.field-label{font-size:8px;color:var(--muted);margin-top:6px}
.field{height:26px;border:1px solid var(--line);border-radius:3px;margin-top:6px;font-size:10px;padding:6px 10px;color:var(--muted)}
.field.active{border-color:#9cc6ee;color:var(--blue)}
.remember{display:flex;align-items:center;gap:5px;font-size:7px;color:var(--muted);margin-top:12px}
.btn{display:flex;align-items:center;justify-content:center;color:var(--white);font-weight:600;border-radius:2px}
.login .btn{background:var(--blue);height:26px;margin-top:14px;font-size:8px}
.forgot{font-size:7px;color:var(--muted);text-align:center;margin-top:14px}

/* shared app chrome */
.topbar{position:absolute;left:0;top:0;width:100%;height:53px;background:var(--ink);color:var(--white)}
.brand{position:absolute;left:53px;top:17px;font-size:16px}
.nav-item{position:absolute;top:22px;font-size:8px;display:flex;align-items:center;gap:4px;color:#dfe2e5}
.footer{position:absolute;left:0;width:100%;height:26px;background:var(--ink);font-size:7px;color:#6b7177;padding:9px 53px}

/* dashboard */
.dashboard{left:191px;top:802px;width:818px;height:720px}
.section-title{position:absolute;left:0;width:100%;text-align:center;font-size:17px;color:var(--ink)}
.program{position:absolute;top:152px;width:218px;text-align:center}
.program-art{height:135px;background:var(--ink)}
.program h3{font-size:12px;font-weight:700;margin-top:18px;color:var(--ink)}
.progress-label{font-size:7px;margin-top:8px}
.bar{height:3px;background:#dcdfe2;margin:5px auto 0;width:120px;position:relative}
.bar span{position:absolute;left:0;top:0;height:3px;background:var(--green)}
.program p{font-size:7.5px;line-height:1.6;color:var(--muted);margin:16px 20px 0;height:36px}
.program .btn{width:110px;height:25px;margin:12px auto 0;font-size:7px;background:var(--blue)}
.program .btn.soon{background:var(--grey-btn)}
.bonuses{position:absolute;left:0;top:494px;width:100%;height:200px;background:var(--soft)}
.bonus{position:absolute;top:108px;width:160px;text-align:center;font-size:8.5px;color:var(--muted)}
.bonus.open{color:var(--text);font-weight:500}
.bonus svg{display:block;margin:0 auto 8px}

/* lesson */
.lesson{left:191px;top:1577px;width:818px;height:906px}
.sidebar{position:absolute;left:0;top:53px;width:272px;height:827px;background:var(--soft)}
.side-center{position:absolute;left:55px;width:157px;text-align:center}
.week-theme{top:27px;font-size:11px;font-weight:700;color:var(--ink)}
.week-sub{top:44px;font-size:8px;color:var(--muted);line-height:1.5}
.week-btn{position:absolute;left:55px;top:119px;width:157px;height:25px;background:var(--blue);color:var(--white);border-radius:13px;font-size:9px;font-weight:700;padding:7px 14px;display:flex;justify-content:space-between;align-items:center}
.lesson-list{position:absolute;left:69px;top:165px;width:186px;list-style:none}
.lesson-list li{height:26px;font-size:7.5px;color:var(--muted);display:flex;justify-content:space-between;align-items:center}
.lesson-list li.current{color:var(--ink);font-weight:600}
.side-pill{position:absolute;left:55px;width:157px;height:25px;background:var(--white);border-radius:13px;font-size:8px;padding:8px 14px;color:var(--text)}
.main{position:absolute;left:327px;top:53px;width:436px}
.kicker{position:absolute;top:30px;font-size:8px}
.lesson-title{position:absolute;top:50px;font-size:14px;color:var(--ink)}
.done-btn{position:absolute;left:328px;top:35px;width:108px;height:25px;background:var(--green);font-size:7px}
.video{position:absolute;top:85px;width:436px;height:244px;background:linear-gradient(135deg,#b9b3aa,#6f737a 55%,#3e444d)}
.video-play{position:absolute;left:198px;top:102px}
.pager{position:absolute;top:329px;width:436px;height:25px;background:#f1f2f3;font-size:6.5px;color:var(--muted);display:flex;justify-content:space-between;align-items:center;padding:0 14px}
.about{position:absolute;top:388px;width:300px;padding-right:18px}
.about h4,.resources h4{font-size:9px;font-weight:600;color:var(--ink)}
.about p{font-size:7px;line-height:1.65;color:var(--muted);margin-top:12px}
.about strong{display:block;font-size:7.5px;color:var(--ink);margin-top:10px}
.about ul{margin:10px 0 0 10px;font-size:7px;line-height:1.68;color:var(--muted)}
.resources{position:absolute;left:300px;top:380px;width:136px;height:218px;border-left:1px solid var(--line);padding:8px 0 0 14px}
.res-item{display:flex;justify-content:space-between;align-items:center;font-size:6.5px;font-weight:700;color:var(--blue);line-height:1.4;padding:14px 0;border-bottom:1px solid var(--line)}
.transcript{position:absolute;top:605px;width:436px;height:177px;border:1px solid var(--line)}
.transcript-head{height:28px;background:#e9eaeb;font-size:8.5px;font-weight:600;padding:9px 14px;display:flex;justify-content:space-between}
.transcript p{font-size:7px;line-height:1.7;color:var(--muted);margin:16px 26px 0 14px}
.transcript .btn{position:absolute;left:14px;top:127px;width:82px;height:27px;background:var(--blue);font-size:7.5px}
</style>
</head>
<body>

<!-- Login screen -->
<section class="screen login">
  <div class="login-photo" role="img" aria-label="Photo of a smiling businessman working on a laptop in a café"></div>
  <div class="login-card">
    <div class="card-head serif">Qentrifold.com</div>
    <div class="card-body">
      <div class="field-label">Enter Your Email</div>
      <div class="field active">name@email.co</div>
      <div class="field-label" style="margin-top:14px">Password</div>
      <div class="field">••••••••</div>
      <div class="remember">
        <svg width="9" height="9" viewBox="0 0 10 10"><circle cx="5" cy="5" r="4.3" fill="none" stroke="#3aa54a"/><path d="M3 5.2l1.4 1.3L7 3.8" fill="none" stroke="#3aa54a"/></svg>
        Remember me
      </div>
      <div class="btn">Login</div>
      <div class="forgot">Forgot Password?</div>
    </div>
  </div>
</section>

<!-- Dashboard -->
<section class="screen dashboard">
  <header class="topbar">
    <div class="brand serif">Qentrifold.com</div>
    <div class="nav-item" style="left:372px"><svg width="8" height="8" viewBox="0 0 10 10"><path d="M5 9L1.2 5.2A2.2 2.2 0 015 2.3a2.2 2.2 0 013.8 2.9z" fill="#fff"/></svg>Refer a Friend</div>
    <div class="nav-item" style="left:474px"><svg width="8" height="8" viewBox="0 0 10 10"><circle cx="5" cy="3" r="2" fill="#fff"/><path d="M1 9a4 4 0 018 0z" fill="#fff"/></svg>Community ⌄</div>
    <div class="nav-item" style="left:580px"><svg width="8" height="8" viewBox="0 0 10 10"><circle cx="5" cy="5" r="4.5" fill="#fff"/></svg>Help ⌄</div>
    <div class="nav-item" style="left:655px"><svg width="8" height="8" viewBox="0 0 10 10"><circle cx="5" cy="3" r="2" fill="#fff"/><path d="M1.5 9a3.5 3.5 0 017 0z" fill="#fff"/></svg>Hi Marlon ⌄</div>
    <div class="nav-item" style="left:757px"><svg width="10" height="10" viewBox="0 0 10 10"><circle cx="4" cy="4" r="3" fill="none" stroke="#fff" stroke-width="1.2"/><path d="M6.3 6.3L9 9" stroke="#fff" stroke-width="1.2"/></svg></div>
  </header>

  <h2 class="section-title serif" style="top:108px">Your Trainingn Programs</h2>

  <article class="program" style="left:55px">
    <div class="program-art" role="img" aria-label="Course cover: large letter C with a small network icon"></div>
    <h3>Brandwell Accelerator</h3>
    <div class="progress-label">11% Complete</div>
    <div class="bar"><span style="width:13px"></span></div>
    <p>How to start and grow a 6-figure Pelwick QRX business with focus on currently dominating with one product.</p>
    <div class="btn">Continue Lesson</div>
  </article>

  <article class="program" style="left:300px">
    <div class="program-art" role="img" aria-label="Course cover: large letter C with a small atom icon"></div>
    <h3>Tierlift Scaling</h3>
    <div class="progress-label">33% Complete</div>
    <div class="bar"><span style="width:40px"></span></div>
    <p>How to scale your business systematically from 6-7 figures using automation and advanced tactics.</p>
    <div class="btn">Continue Lesson</div>
  </article>

  <article class="program" style="left:547px">
    <div class="program-art" role="img" aria-label="Course cover: large letter C with two atom icons"></div>
    <h3>Vantor Mastermind</h3>
    <div class="progress-label">11% Complete</div>
    <div class="bar"><span style="width:13px"></span></div>
    <p>Completely dominate multiple markets. Make 8 figures and eventually sell your empire for a huge cash exit.</p>
    <div class="btn soon">Coming Soon</div>
  </article>

  <section class="bonuses">
    <h2 class="section-title serif" style="top:58px">Your Vip Bonuses</h2>
    <div class="bonus open" style="left:84px">
      <svg width="16" height="20" viewBox="0 0 16 20"><path d="M4 8V5a4 4 0 017.6-1.6" fill="none" stroke="#3aa54a" stroke-width="1.6"/><rect x="2" y="8" width="12" height="11" rx="5" fill="none" stroke="#3aa54a" stroke-width="1.6"/><circle cx="8" cy="13.5" r="1.5" fill="#3aa54a"/></svg>
      Qentri U Plazzo Ads
    </div>
    <div class="bonus" style="left:329px">
      <svg width="16" height="20" viewBox="0 0 16 20"><path d="M4 8V5a4 4 0 018 0v3" fill="none" stroke="#aab0b5" stroke-width="1.6"/><rect x="2" y="8" width="12" height="11" rx="5" fill="none" stroke="#aab0b5" stroke-width="1.6"/><circle cx="8" cy="13.5" r="1.5" fill="#aab0b5"/></svg>
      KT approved product<br>pick list
    </div>
    <div class="bonus" style="left:576px">
      <svg width="16" height="20" viewBox="0 0 16 20"><path d="M4 8V5a4 4 0 018 0v3" fill="none" stroke="#aab0b5" stroke-width="1.6"/><rect x="2" y="8" width="12" height="11" rx="5" fill="none" stroke="#aab0b5" stroke-width="1.6"/><circle cx="8" cy="13.5" r="1.5" fill="#aab0b5"/></svg>
      All in one package
    </div>
  </section>

  <footer class="footer" style="top:694px">©2018 Qentrifold.com</footer>
</section>

<!-- Lesson page -->
<section class="screen lesson">
  <header class="topbar">
    <div class="brand serif">Qentrifold.com</div>
    <div class="nav-item" style="left:372px"><svg width="8" height="8" viewBox="0 0 10 10"><path d="M5 9L1.2 5.2A2.2 2.2 0 015 2.3a2.2 2.2 0 013.8 2.9z" fill="#fff"/></svg>Refer a Friend</div>
    <div class="nav-item" style="left:474px"><svg width="8" height="8" viewBox="0 0 10 10"><circle cx="5" cy="3" r="2" fill="#fff"/><path d="M1 9a4 4 0 018 0z" fill="#fff"/></svg>Community ⌄</div>
    <div class="nav-item" style="left:580px"><svg width="8" height="8" viewBox="0 0 10 10"><circle cx="5" cy="5" r="4.5" fill="#fff"/></svg>Help ⌄</div>
    <div class="nav-item" style="left:655px"><svg width="8" height="8" viewBox="0 0 10 10"><circle cx="5" cy="3" r="2" fill="#fff"/><path d="M1.5 9a3.5 3.5 0 017 0z" fill="#fff"/></svg>Hi Marlon ⌄</div>
    <div class="nav-item" style="left:757px"><svg width="10" height="10" viewBox="0 0 10 10"><circle cx="4" cy="4" r="3" fill="none" stroke="#fff" stroke-width="1.2"/><path d="M6.3 6.3L9 9" stroke="#fff" stroke-width="1.2"/></svg></div>
  </header>

  <aside class="sidebar">
    <div class="side-center week-theme">Week Theme</div>
    <div class="side-center week-sub">Three Proven Conversion<br>Funnels</div>
    <div class="side-center" style="top:82px;font-size:7px">
      <div class="bar" style="width:157px;margin:0"><span style="width:34px"></span></div>
      <div style="margin-top:6px">33% Complete</div>
    </div>
    <div class="week-btn">Week Five <span>⌄</span></div>
    <ul class="lesson-list">
      <li>1. Assembling the Machines <svg width="9" height="9" viewBox="0 0 10 10"><circle cx="5" cy="5" r="4.3" fill="none" stroke="#3aa54a"/><path d="M3 5.2l1.4 1.3L7 3.8" fill="none" stroke="#3aa54a"/></svg></li>
      <li>2. VSL Overview &amp; Math <svg width="9" height="9" viewBox="0 0 10 10"><circle cx="5" cy="5" r="4.3" fill="none" stroke="#3aa54a"/><path d="M3 5.2l1.4 1.3L7 3.8" fill="none" stroke="#3aa54a"/></svg></li>
      <li>3. VSL Pages &amp; Automation <svg width="9" height="9" viewBox="0 0 10 10"><circle cx="5" cy="5" r="4.3" fill="none" stroke="#3aa54a"/><path d="M3 5.2l1.4 1.3L7 3.8" fill="none" stroke="#3aa54a"/></svg></li>
      <li class="current">4. JIT Overview &amp; Math <svg width="9" height="9" viewBox="0 0 10 10"><circle cx="5" cy="5" r="4.3" fill="none" stroke="#3aa54a"/><path d="M3 5.2l1.4 1.3L7 3.8" fill="none" stroke="#3aa54a"/></svg></li>
      <li>5. JIT Pages &amp; Automation <svg width="9" height="9" viewBox="0 0 10 10"><circle cx="5" cy="5" r="4.3" fill="none" stroke="#3aa54a"/><path d="M3 5.2l1.4 1.3L7 3.8" fill="none" stroke="#3aa54a"/></svg></li>
      <li>6. 2KA Overview &amp; Math <svg width="9" height="9" viewBox="0 0 10 10"><circle cx="5" cy="5" r="4.3" fill="none" stroke="#3aa54a"/><path d="M3 5.2l1.4 1.3L7 3.8" fill="none" stroke="#3aa54a"/></svg></li>
      <li>7. 2KA Pages &amp; Automation <svg width="9" height="9" viewBox="0 0 10 10"><circle cx="5" cy="5" r="4.3" fill="none" stroke="#3aa54a"/><path d="M3 5.2l1.4 1.3L7 3.8" fill="none" stroke="#3aa54a"/></svg></li>
    </ul>
    <div class="side-pill" style="top:365px">Action Items</div>
    <div class="side-pill" style="top:407px">Questions</div>
  </aside>

  <main class="main">
    <div class="kicker">Tierlift Scaling</div>
    <h1 class="lesson-title serif">4. JIT Overview &amp; Math</h1>
    <div class="btn done-btn">Lesson Completed</div>

    <div class="video" role="img" aria-label="Lesson video still: presenter seated in a bright office">
      <svg class="video-play" width="40" height="40" viewBox="0 0 40 40"><circle cx="20" cy="20" r="18" fill="rgba(255,255,255,.15)" stroke="#fff" stroke-width="2"/><path d="M16 12l12 8-12 8z" fill="#fff"/></svg>
    </div>
    <div class="pager"><span>←&nbsp;&nbsp; PREV LESSON</span><span style="color:var(--ink)">NEXT LESSON &nbsp;&nbsp;→</span></div>

    <section class="about">
      <h4>About this Lesson</h4>
      <p>Pri quas audiam virtute ut, case utamur fuisset eam ut, iisque accommodare an eam. Reque blandit qui eu cu vix nonumy volutpat. Legendos intellegam id usu, vide oporteat vix eu, id illud principes has. Nam tempor utamur gubergren no.</p>
      <strong>Here's what we Cover:</strong>
      <ul>
        <li>The JIT Funnel - What it is and why we use it</li>
        <li>The JIT Funnel - The fundamental math that drives it</li>
        <li>The JIT Funnel - A high-level of how it works</li>
        <li>The JIT Funnel - A high-level of how it works</li>
        <li>The JIT Funnel - Measuring and tracking performance</li>
        <li>The JIT Funnel - Troubleshooting issues</li>
      </ul>
    </section>

    <aside class="resources">
      <h4>Resources</h4>
      <div class="res-item">THE JIT WEBINAR<br>FUNNEL <svg width="20" height="20" viewBox="0 0 20 20"><circle cx="10" cy="10" r="9" fill="#1c74c9"/><path d="M10 5v8M6.5 9.5L10 13l3.5-3.5M6 15h8" fill="none" stroke="#fff" stroke-width="1.3"/></svg></div>
      <div class="res-item" style="border:0">JIT FUNNEL<br>TRACKING SHEET <svg width="20" height="20" viewBox="0 0 20 20"><circle cx="10" cy="10" r="9" fill="none" stroke="#1c74c9"/><path d="M10 5v8M6.5 9.5L10 13l3.5-3.5M6 15h8" fill="none" stroke="#1c74c9" stroke-width="1.3"/></svg></div>
    </aside>

    <section class="transcript">
      <div class="transcript-head"><span>Full Video Transcript / Mp3</span><span style="color:var(--muted)">⤢</span></div>
      <p>Lorem ipsum dolor sit amet, consectetur adipisicing elit, sed do eiusmod tempor incididunt ut labore et dolore magna aliqua. Ut enim ad minim veniam, quis nostrud exercitation ullamco laboris nisi ut aliquip ex ea commodo consequat. Duis aute irure dolor in reprehenderit in voluptate velit esse cillum dolore eu fugiat nulla pariatur. Excepteur sint occaecat cupidatat non proident, sunt in culpa qui officia deserunt mollit anim id est laborum.</p>
      <div class="btn">Read More</div>
    </section>
  </main>

  <footer class="footer" style="top:880px">©2018 Qentrifold.com</footer>
</section>

</body>
</html>
```